Doctors Office Web Design

Name of the business is Lian-Hua Qiu M.D.
We need a web design that is attractive for women that want to see Dr. Lian-Hua Qiu for Obstetrician Gynecology and Pregnancy care. Dr. Qiu earned her degree from Harbor Crest Medical College of obstetrician gynecology. We want to attract women of child bearing ages to come to our offices for health, education, and pregnancies.

Please visit http://www.drqiucare-example.com/ to help you get a feel for who we are. We will be adding some pictures and logo in the next few days.

We are looking for to have pages for and tabs including
About Us- History, Our Staff, Dr. Qiu
Patient Information- Appointments, E-Prescriptions, Payments Accepted, Insurance
Health- General, Sexual, Mental, Affiliates
Pregnancy- Minimally invasive surgery(our specialty), 4-D Ultra Sound, Hospital Affiliations
Media- News,Pictures, Videos
Locations- Palmvale Office, Marlow Office

The colors we would like to use are pastel colors, magenta, and plum

Target Market(s)

Women of all ages with an emphasis on 25-65 year olds

Industry/Entity Type

Business

Requirements
Must have
• Needs to include a location for a our videos and pictures that I will submit shortly. We also want a map to our location or atleast a place for one.
Nice to have
• A place for a google map of our office locations.

```html
<!DOCTYPE html>
<html lang="en">
<head>
<meta charset="utf-8">
<title>Lian-Hua Qiu M.D. — Obstetrics &amp; Gynecology</title>
<link href="https://fonts.googleapis.com/css2?family=Arimo:wght@400;700&family=Open+Sans:wght@400;600&family=PT+Sans+Narrow:wght@400;700&family=PT+Sans:wght@400;700&display=swap" rel="stylesheet">
<style>
  :root{
    --plum:#8e3b80;
    --plum-dark:#6f2a64;
    --magenta:#f07ab8;
    --orchid:#a5569b;
    --sky:#e7f0f8;
    --steel:#7f9cb6;
    --teal:#4fa3c9;
    --text:#7a7a7a;
    --line:#cfdbe6;
    --card:#eef7f8;
    --card-line:#bfd6e4;
    --white:#ffffff;
  }
  *{box-sizing:border-box;margin:0;padding:0}
  html,body{width:1200px;height:1068px;overflow:hidden;background:var(--white)}
  body{position:relative;font-family:"Open Sans",Arial,sans-serif;color:var(--text)}
  a{text-decoration:none;color:inherit}

  /* header */
  .site-header{position:absolute;left:0;top:0;width:1200px;height:107px;background:var(--white);box-shadow:0 3px 6px rgba(0,0,0,.08);z-index:3}
  .brand{position:absolute;left:73px;top:18px;display:flex;gap:12px}
  .brand-dot{width:26px;height:26px;border-radius:50%;background:var(--teal);margin-top:4px}
  .brand-name{font-family:"PT Sans",Arial,sans-serif;font-weight:700;font-size:28px;color:var(--orchid);letter-spacing:.5px;line-height:34px}
  .brand-sub{position:absolute;left:117px;top:53px;font-family:"PT Sans",Arial,sans-serif;font-size:15px;line-height:19px;color:#6e9cbd}
  .main-nav{position:absolute;right:92px;top:56px;display:flex;align-items:center;font-family:Arimo,Arial,sans-serif;font-size:17px;color:var(--plum)}
  .main-nav a{line-height:37px}
  .main-nav .sep{margin:0 14px}
  .main-nav .active{background:var(--plum);color:var(--white);border-radius:6px;padding:0 16px;margin:0 22px 0 16px;height:38px}

  /* hero */
  .hero{position:absolute;left:0;top:107px;width:1200px;height:353px;background:linear-gradient(180deg,#eaf2fa,#e3edf7);border-bottom:1px solid var(--line)}
  .hero-title{position:absolute;left:159px;top:92px;font-family:"PT Sans Narrow",Arial,sans-serif;font-weight:700;font-size:27px;color:var(--steel);letter-spacing:.6px}
  .hero-lead{position:absolute;left:288px;top:143px;font-family:"PT Sans Narrow",Arial,sans-serif;font-weight:700;font-size:17px;line-height:21px;color:var(--steel);letter-spacing:.3px}
  .hero-button{position:absolute;left:287px;top:201px;width:180px;height:56px;border-radius:7px;background:#c9dbee;padding:4px}
  .hero-button span{display:block;height:100%;border-radius:5px;background:linear-gradient(180deg,#a8549c,#7d2f6f);color:var(--white);font-family:"PT Sans Narrow",Arial,sans-serif;font-weight:700;font-size:22px;text-align:center;line-height:48px;letter-spacing:.5px}
  .hero-instrument{position:absolute;left:120px;top:146px;width:148px;height:148px;border-radius:50%;background:radial-gradient(circle,#c9d6e6 0%,#dbe6f2 60%,rgba(227,237,247,0) 72%)}
  .hero-photo{position:absolute;left:765px;top:48px;width:346px;height:346px;border-radius:50%;border:5px solid var(--magenta);background:linear-gradient(120deg,#fbe9f1 0%,#f3c1d6 40%,#e05d9a 75%,#c93f83 100%)}
  .bubble{position:absolute;border-radius:50%;display:flex;align-items:center;justify-content:center;text-align:center;color:var(--white)}
  .bubble-services{left:632px;top:65px;width:234px;height:234px;background:radial-gradient(circle at 40% 30%,#a4579a,#7c2d6e);border:3px solid #e8d7ea;font-size:18px;line-height:22px}
  .bubble-surgery{left:746px;top:280px;width:124px;height:124px;background:radial-gradient(circle at 40% 30%,#5db4d8,#3a8fbe);border:3px solid #dbecf5;font-size:17px;line-height:21px}

  /* content */
  .welcome{position:absolute;left:91px;top:500px;width:700px}
  .welcome h1,.welcome h2{font-family:Arimo,Arial,sans-serif;font-weight:400;color:var(--orchid);font-size:23px}
  .welcome p{font-size:14px;line-height:25px;color:var(--text)}
  .welcome .intro{margin-top:8px}
  .welcome h2{margin-top:24px;font-size:22px}
  .welcome .services{margin-top:4px}
  .welcome .contact{margin-top:28px}

  .side-box{position:absolute;left:823px;top:530px;width:270px;height:203px;border:1px solid #c9c9d2;background:var(--white)}
  .side-box h3{height:37px;margin:-1px -1px 0;background:linear-gradient(180deg,#a24f96,#7e3070);color:var(--white);font-family:"PT Sans",Arial,sans-serif;font-weight:400;font-size:17px;line-height:37px;padding-left:24px;letter-spacing:.3px}
  .side-box ul{list-style:none;padding:16px 0 0 14px}
  .side-box li{display:flex;align-items:center;gap:14px;height:32.5px;font-size:14.5px}
  .side-box svg{flex:none}

  /* footer */
  .site-footer{position:absolute;left:0;top:809px;width:1200px;height:259px;background:linear-gradient(180deg,#dfeaf5,#e8f0f8)}
  .footer-edge{position:absolute;left:0;top:-8px}
  .office-card{position:absolute;top:43px;height:132px;border:1px solid var(--card-line);border-radius:6px;background:var(--card);font-family:Arimo,Arial,sans-serif;font-size:13.5px;color:var(--plum);padding:18px 0 0 33px;line-height:25px}
  .office-card.marlow{left:68px;width:340px}
  .office-card.palmvale{left:400px;width:296px}
  .office-card .line{display:flex;align-items:center;gap:10px}
  .office-card .icon-row{padding-left:9px}
  .copyright{position:absolute;left:209px;top:199px;font-family:Arimo,Arial,sans-serif;font-size:13px;color:var(--plum)}
  .copyright .sep{margin:0 10px}
  .office-map{position:absolute;left:985px;top:40px;width:130px;height:120px;border:1px solid var(--card-line);border-radius:6px;background:linear-gradient(160deg,#f1f6f9,#dce8f1)}
</style>
</head>
<body>

<header class="site-header">
  <div class="brand">
    <span class="brand-dot"></span>
    <span class="brand-name">LIAN-HUA QIU M.D.</span>
  </div>
  <div class="brand-sub">Board certified<br>Obstetrician/Gynecologist</div>
  <nav class="main-nav">
    <a href="#">Home</a><span class="sep">|</span>
    <a href="#">About us</a>
    <a href="#" class="active">Patient Information</a>
    <a href="#">Health</a><span class="sep">|</span>
    <a href="#">Pregnancy</a><span class="sep">|</span>
    <a href="#">Media</a><span class="sep">|</span>
    <a href="#">Locations</a>
  </nav>
</header>

<section class="hero">
  <div class="hero-title">DR. QIU’S CARE PHILOSOPHY IS</div>
  <div class="hero-lead">TO ENSURE THE HIGHEST LEVEL OF<br>PATIENT EDUCATION.</div>
  <div class="hero-instrument" role="img" aria-label="Illustration of a stethoscope"></div>
  <a class="hero-button" href="#"><span>READ MORE</span></a>
  <div class="hero-photo" role="img" aria-label="Photo of a pregnant woman in a pink top holding her belly"></div>
  <div class="bubble bubble-services">Obstetrics,<br>Family Planning,<br>Hormonal Evaluation,<br>Incontinence,<br>Infertility</div>
  <div class="bubble bubble-surgery">Gynecology<br>Surgery</div>
</section>

<main class="welcome">
  <h1>Welcome to Dr. Lian-Hua Qiu's website.</h1>
  <p class="intro">Welcome to Dr. Lian-Hua Qiu's website. Here you will be able to find information about both of our offices, meet Dr. Qiu and her staff, and browse through our women's health links to learn more about pregnancy, nutrition, exercise, and other women's health issues. Have fun and if you have any questions, feel free to contact us at drqiu@harborlink-example.net</p>
  <h2>Serving All Areas of Women's Health, including:</h2>
  <p class="services">Obstetrics, Family Planning, Hormonal Evaluation, Incontinence, Infertility, and Gynecology Surgery</p>
  <p class="contact">Contact us!&nbsp; Send e-mail to drqiu@harborlink-example.net with your comments and suggestions for this site.</p>
</main>

<aside class="side-box">
  <h3>OFFICE LOCATIONS</h3>
  <ul>
    <li><svg width="14" height="14" viewBox="0 0 14 14"><circle cx="7" cy="7" r="7" fill="#9b4d90"/><path d="M4 7.2l2 2 4-4.2" stroke="#fff" stroke-width="1.8" fill="none"/></svg>About the Practice</li>
    <li><svg width="14" height="14" viewBox="0 0 14 14"><circle cx="7" cy="7" r="7" fill="#9b4d90"/><path d="M4 7.2l2 2 4-4.2" stroke="#fff" stroke-width="1.8" fill="none"/></svg>Meet Dr. Qiu</li>
    <li><svg width="14" height="14" viewBox="0 0 14 14"><circle cx="7" cy="7" r="7" fill="#9b4d90"/><path d="M4 7.2l2 2 4-4.2" stroke="#fff" stroke-width="1.8" fill="none"/></svg>OB/GYN Info.</li>
    <li><svg width="14" height="14" viewBox="0 0 14 14"><circle cx="7" cy="7" r="7" fill="#9b4d90"/><path d="M4 7.2l2 2 4-4.2" stroke="#fff" stroke-width="1.8" fill="none"/></svg>The Pregnancy Page</li>
  </ul>
</aside>

<footer class="site-footer">
  <svg class="footer-edge" width="1200" height="10" viewBox="0 0 1200 10" preserveAspectRatio="none">
    <defs><pattern id="edge-teeth" width="12" height="10" patternUnits="userSpaceOnUse"><path d="M0 10 L6 2 L12 10 Z" fill="#dfeaf5"/></pattern></defs>
    <rect width="1200" height="10" fill="url(#edge-teeth)"/>
  </svg>

  <div class="office-card marlow">
    <div>4780 Lantern Grove Avenue, Suite 204-205</div>
    <div>Marlow Shores, Florida&nbsp; 33901</div>
    <div class="line icon-row"><svg width="13" height="15" viewBox="0 0 13 15"><rect x="1" y="0" width="11" height="15" rx="2" fill="#8e3b80"/><rect x="3" y="2" width="7" height="5" fill="#eef7f8"/></svg>Telephone:&nbsp; (555) 014-2231</div>
    <div class="line"><svg width="16" height="15" viewBox="0 0 16 15"><rect x="0" y="4" width="16" height="11" rx="2" fill="#8e3b80"/><rect x="4" y="0" width="8" height="6" fill="#b77aaf"/></svg>Fax:&nbsp; (555) 014-2298</div>
  </div>

  <div class="office-card palmvale">
    <div>218 N.W. 9th Terrace, Suite 310B</div>
    <div>Palmvale, Florida&nbsp; 33912</div>
    <div class="line icon-row"><svg width="13" height="15" viewBox="0 0 13 15"><rect x="1" y="0" width="11" height="15" rx="2" fill="#8e3b80"/><rect x="3" y="2" width="7" height="5" fill="#eef7f8"/></svg>Telephone:&nbsp; (555) 016-7740</div>
    <div class="line"><svg width="16" height="15" viewBox="0 0 16 15"><rect x="0" y="4" width="16" height="11" rx="2" fill="#8e3b80"/><rect x="4" y="0" width="8" height="6" fill="#b77aaf"/></svg>Fax:&nbsp; (555) 016-7785</div>
  </div>

  <div class="copyright">(c) Copyright 2002, Lian-Hua Qiu, M.D., P.A .<span class="sep">|</span>Disclaimer</div>

  <div class="office-map" role="img" aria-label="Map of the Marlow and Palmvale office locations"></div>
</footer>

</body>
</html>
```